Classy business card for accounting firm

We're looking for a new business card for our accounting firm. Our logo was designed by Brandolith, so all of the design info we would like to use has been provided. The specific font provided isn't required to be used.

We want the card to look classy and elegent. Probably more minimalistic, but still with some pops of color.

The options we would like to include on the card are as follows:
1. Main office phone line
2. Direct phone line
3. Email address
4. Website URL
5. Name
6. Title (CEO, President, etc.)
7. Firm Address

The design and card should be double sided!!! The drop down box in the project brief for some reason is defaulting to single sided. Not sure why this is happening.

Thanks!

Contact Information for Business Card

The options we would like to include on the card are as follows: 1. Main office phone line 2. Direct phone line 3. Email address 4. Website URL 5. Name 6. Title (CEO, President, etc.) 7. Firm Address

Requirements
Must have
• Card must be double sided.

```html
<!DOCTYPE html>
<html lang="en">
<head>
<meta charset="utf-8">
<title>Ledgerline Associates – Business Card</title>
<link rel="stylesheet" href="https://fonts.googleapis.com/css2?family=Montserrat:wght@400;500;600&display=swap">
<style>
  :root {
    --backdrop: #fbe9dc;
    --card-white: #ffffff;
    --peach: #fde5cc;
    --olive: #b5c043;
    --olive-light: #d2d97e;
    --orange: #f47a12;
    --ink: #666666;
    --ink-soft: #555555;
  }
  * { box-sizing: border-box; margin: 0; padding: 0; }
  html, body {
    width: 973px; height: 1200px; overflow: hidden;
    background: var(--backdrop);
    font-family: "Montserrat", Arial, sans-serif;
    color: var(--ink);
  }
  .card {
    position: absolute; left: 123px;
    width: 727px; height: 427px;
    background: var(--card-white);
    overflow: hidden;
    box-shadow: 0 18px 30px rgba(90, 70, 50, 0.28);
  }
  .card--front { top: 127px; }
  .card--back { top: 652px; }
  .card__art { position: absolute; inset: 0; width: 100%; height: 100%; }

  .person { position: absolute; left: 43px; top: 40px; }
  .person__name { font-size: 35px; font-weight: 500; color: var(--ink); letter-spacing: 0.2px; }
  .person__title { font-size: 17px; font-weight: 400; margin-top: 6px; color: var(--ink-soft); }

  .contact { position: absolute; left: 43px; list-style: none; }
  .contact__item { display: flex; align-items: center; height: 40px; margin-bottom: 33px; }
  .contact__icon { width: 40px; height: 40px; flex: none; }
  .contact__text { margin-left: 17px; font-size: 17px; line-height: 22px; color: var(--ink-soft); }

  .front-name {
    position: absolute; left: 428px; top: 178px; width: 180px;
    text-align: center; font-size: 24px; font-weight: 600; line-height: 32px;
    color: var(--orange); letter-spacing: 1px;
  }

  .brand { position: absolute; left: 0; right: 0; top: 128px; text-align: center; }
  .brand__square { width: 62px; height: 62px; margin: 0 auto 40px; background: var(--orange); }
  .brand__name { font-size: 33px; font-weight: 500; color: var(--ink); letter-spacing: 1.5px; }
  .brand__tagline {
    display: flex; align-items: center; justify-content: center; gap: 14px;
    margin-top: 8px; font-size: 16px; font-weight: 500; letter-spacing: 1.6px; color: var(--ink-soft);
  }
  .brand__rule { width: 70px; height: 2px; background: var(--olive); }
</style>
</head>
<body>

<section class="card card--front" aria-label="Business card front">
  <svg class="card__art" viewBox="0 0 727 427" aria-hidden="true">
    <defs>
      <linearGradient id="bandFadeA" x1="0" y1="1" x2="1" y2="0">
        <stop offset="0" stop-color="#b5c043"/>
        <stop offset="1" stop-color="#b5c043" stop-opacity="0.15"/>
      </linearGradient>
    </defs>
    <polygon points="557,0 727,0 727,427 174,427" fill="var(--peach)"/>
    <polygon points="508,0 570,0 540,30" fill="var(--olive)"/>
    <polygon points="600,0 680,0 590,100 525,100" fill="url(#bandFadeA)"/>
    <polygon points="710,55 727,55 727,150 665,215 635,190" fill="url(#bandFadeA)"/>
    <polygon points="727,230 727,290 605,427 520,427" fill="url(#bandFadeA)"/>
    <polygon points="727,330 727,390 692,427 640,427" fill="var(--olive-light)"/>
  </svg>

  <div class="person">
    <h1 class="person__name">Laura J Benton</h1>
    <p class="person__title">Office Administrator</p>
  </div>

  <ul class="contact" style="top:187px;">
    <li class="contact__item">
      <svg class="contact__icon" viewBox="0 0 40 40" aria-hidden="true">
        <circle cx="20" cy="20" r="18.5" fill="none" stroke="var(--orange)" stroke-width="1.5"/>
        <path d="M14 12.5l3 -1 2.5 5 -2 1.5c1 2.5 3 4.5 5.5 5.5l1.5 -2 5 2.5 -1 3c-7 0.5 -14.5 -7 -14.5 -14.5z" fill="none" stroke="var(--orange)" stroke-width="1.4" stroke-linejoin="round"/>
      </svg>
      <span class="contact__text">206 555-0148<br>206 555-0173</span>
    </li>
    <li class="contact__item">
      <svg class="contact__icon" viewBox="0 0 40 40" aria-hidden="true">
        <circle cx="20" cy="20" r="18.5" fill="none" stroke="var(--orange)" stroke-width="1.5"/>
        <g fill="none" stroke="var(--orange)" stroke-width="1.3">
          <circle cx="20" cy="20" r="8.5"/>
          <ellipse cx="20" cy="20" rx="3.8" ry="8.5"/>
          <path d="M11.5 20h17M13 15.5h14M13 24.5h14"/>
        </g>
      </svg>
      <span class="contact__text">benton@ledgerline.cc<br>http://www.ledgerline.cc</span>
    </li>
    <li class="contact__item">
      <svg class="contact__icon" viewBox="0 0 40 40" aria-hidden="true">
        <circle cx="20" cy="20" r="18.5" fill="none" stroke="var(--orange)" stroke-width="1.5"/>
        <path d="M20 29c-4 -5 -6.5 -8.5 -6.5 -11.5a6.5 6.5 0 0 1 13 0c0 3 -2.5 6.5 -6.5 11.5z" fill="none" stroke="var(--orange)" stroke-width="1.4"/>
        <circle cx="20" cy="17.5" r="2.3" fill="none" stroke="var(--orange)" stroke-width="1.3"/>
      </svg>
      <span class="contact__text">418 Alder Ave.<br>Seattle, WA 98101</span>
    </li>
  </ul>

  <p class="front-name">LEDGERLINE<br>ASSOCIATES</p>
</section>

<section class="card card--back" aria-label="Business card back">
  <svg class="card__art" viewBox="0 0 727 427" aria-hidden="true">
    <defs>
      <linearGradient id="bandFadeB" x1="1" y1="0" x2="0" y2="1">
        <stop offset="0" stop-color="#b5c043"/>
        <stop offset="1" stop-color="#b5c043" stop-opacity="0.12"/>
      </linearGradient>
      <linearGradient id="bandFadeC" x1="0" y1="1" x2="1" y2="0">
        <stop offset="0" stop-color="#b5c043"/>
        <stop offset="1" stop-color="#b5c043" stop-opacity="0.15"/>
      </linearGradient>
    </defs>
    <polygon points="528,0 727,0 727,427 101,427" fill="var(--peach)"/>
    <polygon points="110,0 215,0 0,185 0,95" fill="url(#bandFadeB)"/>
    <polygon points="0,0 60,0 0,55" fill="var(--olive-light)"/>
    <polygon points="225,0 290,0 60,195 30,170" fill="url(#bandFadeB)" opacity="0.7"/>
    <polygon points="727,215 727,275 585,427 505,427" fill="url(#bandFadeC)"/>
    <polygon points="727,320 727,380 683,427 625,427" fill="var(--olive-light)"/>
  </svg>

  <div class="brand">
    <div class="brand__square"></div>
    <h2 class="brand__name">LEDGERLINE ASSOCIATES</h2>
    <p class="brand__tagline"><span class="brand__rule"></span>SOLVING TAX PROBLEMS<span class="brand__rule"></span></p>
  </div>
</section>

</body>
</html>
```